I'm looking for strong image and design for the first book in a series titled "Bernard Whitcombe On A Voyage Through Our Convictions" subtitle "Finding a Footing in Living"; although it's about beliefs, I'm not look for an ethereal feel as the first book is about how our beliefs impact our actions and expectations. I'm a published philosopher and keen on branding my name for professional purposes hence the use of my name :) The book will initially be an e-book but I will follow up with a paperback soon afterwards. My website http://bernardwhitcombe-example.com/ may provide some help on me and my projects. Thanks, Bern

Target Market(s)

Graduates and corporate folk who tend to lose their way in the systems.

Logo Text

Bernard Whitcombe on Convictions

Font styles to use
Sans Serif

Colors

Designer to choose colors to be used in the design.

Requirements
Must have
• Needless to say, but impact.
Nice to have
• Strong colours
Should not have
• Religious imagery; the book is philosophical and leans into living in this world.

```html
<!DOCTYPE html>
<html lang="en">
<head>
<meta charset="utf-8">
<title>Bernard Whitcombe On A Voyage Through Our Convictions — Cover Wrap</title>
<link rel="stylesheet" href="https://fonts.googleapis.com/css2?family=Cinzel:wght@400;600&family=EB+Garamond:wght@400;500&display=swap">
<style>
  :root {
    --gold: #e9b318;
    --ink-white: #ffffff;
    --sky-top: #0b1322;
    --sky-mid: #3a3d46;
    --ridge: #050505;
    --glow: #e2c21e;
    --field-light: #b59a2a;
    --field-mid: #5f6a2a;
    --field-dark: #1f2a14;
    --spine: rgba(120, 118, 40, 0.55);
    --barcode-box: #ffffff;
  }
  * { margin: 0; padding: 0; box-sizing: border-box; }
  html, body { width: 1200px; height: 860px; overflow: hidden; background: #000; }
  .cover-wrap {
    position: relative;
    width: 1200px;
    height: 860px;
    overflow: hidden;
  }
  .scene {
    position: absolute;
    inset: 0;
    background:
      radial-gradient(ellipse 170px 70px at 790px 395px, rgba(240, 205, 40, 0.95), rgba(200, 170, 20, 0.35) 55%, transparent 100%),
      radial-gradient(ellipse 260px 110px at 900px 520px, rgba(235, 195, 40, 0.55), transparent 100%),
      radial-gradient(ellipse 140px 260px at 740px 120px, rgba(190, 190, 205, 0.35), transparent 100%),
      linear-gradient(to bottom,
        var(--sky-top) 0%,
        var(--sky-mid) 30%,
        #1a1a1c 40%,
        var(--ridge) 46%,
        var(--ridge) 56%,
        #6a6a28 62%,
        var(--field-mid) 70%,
        #3f4a1e 84%,
        var(--field-dark) 100%);
  }
  .spine {
    position: absolute;
    left: 574px;
    top: 0;
    width: 52px;
    height: 860px;
    background: var(--spine);
    display: flex;
    justify-content: center;
    padding-top: 26px;
  }
  .spine-text {
    writing-mode: vertical-rl;
    color: var(--ink-white);
    white-space: nowrap;
    display: flex;
    align-items: center;
  }
  .spine-title {
    font-family: "Cinzel", serif;
    font-size: 16.5px;
    letter-spacing: 0.5px;
  }
  .spine-subtitle {
    font-family: "EB Garamond", serif;
    font-size: 17px;
    margin-top: 38px;
  }
  .back-title {
    position: absolute;
    left: 90px;
    width: 400px;
    top: 98px;
    text-align: center;
    font-family: "Cinzel", serif;
    font-size: 17px;
    line-height: 23px;
    color: var(--ink-white);
  }
  .back-blurb {
    position: absolute;
    left: 104px;
    width: 360px;
    top: 210px;
    text-align: center;
    font-family: "EB Garamond", serif;
    font-size: 14.3px;
    line-height: 19px;
    color: var(--ink-white);
  }
  .publisher-mark {
    position: absolute;
    left: 62px;
    top: 690px;
    display: flex;
    align-items: center;
    gap: 10px;
    font-family: "Cinzel", serif;
    font-weight: 400;
    font-size: 21px;
    line-height: 23px;
    color: var(--gold);
  }
  .publisher-mark .dot {
    width: 22px;
    height: 22px;
    border-radius: 50%;
    background: var(--gold);
  }
  .barcode-space {
    position: absolute;
    left: 336px;
    top: 649px;
    width: 211px;
    height: 113px;
    background: var(--barcode-box);
  }
  .front-title {
    position: absolute;
    left: 626px;
    width: 574px;
    top: 36px;
    text-align: center;
    font-family: "Cinzel", serif;
    font-weight: 600;
    color: var(--gold);
    text-shadow: 0 2px 6px rgba(0, 0, 0, 0.5);
  }
  .front-title .author { display: block; font-size: 66px; line-height: 76px; }
  .front-title .series-line { display: block; font-weight: 400; font-size: 40px; line-height: 52px; }
  .front-title .series-line.first { margin-top: 16px; }
  .front-subtitle {
    position: absolute;
    left: 626px;
    width: 574px;
    top: 384px;
    text-align: center;
    font-family: "EB Garamond", serif;
    font-weight: 500;
    font-size: 30px;
    color: var(--ink-white);
    text-shadow: 0 2px 4px rgba(0, 0, 0, 0.6);
  }
</style>
</head>
<body>
  <main class="cover-wrap">
    <div class="scene" role="img" aria-label="Photograph spanning the wrap: starry night sky with the Milky Way above dark mountains, a yellow glow in the valley, and a golden field with a wet dirt track on which a hiker with a hat and backpack walks away"></div>

    <section class="back-cover">
      <h2 class="back-title">Bernard Whitcombe On<br>A Voyage Through Our Convictions</h2>
      <p class="back-blurb">Lorem ipsum dolor sit amet, consectetur adipiscing elit, sed do eiusmod tempor incididunt ut labore et dolore magna aliqua. Ut enim ad minim veniam, quis nostrud exercitation ullamco laboris nisi ut aliquip ex ea commodo consequat. Duis aute irure dolor in reprehenderit in voluptate velit esse cillum dolore eu fugiat nulla pariatur. Excepteur sint occaecat cupidatat non proident, sunt in culpa qui officia deserunt mollit anim id est laborum</p>
      <div class="publisher-mark">
        <span class="dot"></span>
        <span>Bernard<br>Whitcombe</span>
      </div>
      <div class="barcode-space"></div>
    </section>

    <aside class="spine">
      <div class="spine-text">
        <span class="spine-title">Bernard Whitcombe On A Voyage Through Our Convictions</span>
        <span class="spine-subtitle">Finding a Footing in Living</span>
      </div>
    </aside>

    <section class="front-cover">
      <h1 class="front-title">
        <span class="author">Bernard</span>
        <span class="author">Whitcombe</span>
        <span class="series-line first">On A Voyage Through</span>
        <span class="series-line">Our Convictions</span>
      </h1>
      <p class="front-subtitle">Finding a Footing in Living</p>
    </section>
  </main>
</body>
</html>
```